Law Firm Banner Ads

Hi, I am an account manager for an Ad Agency that is looking for new Banner ads for a client of ours, The Brandt Law Firm. We would like new ads for their Display Campaigns. The Law Firm Specializes in Criminal Defense, DUIs and a bunch of other stuff. We would like the ads to either list a few key areas or focus on just one area, like DUIs. It is up to you guys on how you would like to do it, and we are open to either approach and simply planning on choosing the one that looks the best and looks like it has the most potential to drive traffic/conversions but we tend to get the best results from designers when we let them have as much freedom as possible. So feel free to make it however you like. We normally ask that the banners match the website because we've seen that congruency helps increase conversion rates, but in this case the website is getting re-made because it is so ugly. If you can match the look of site without making ugly ads, your chances of winning probably do increase, or maybe try to match the mobile site instead of the desktop stie. On the other hand, if you make ads that are super awesome/unique and don't look like the site, your chances of winning can increase as well.
Also feel free to use any text or call to action buttons that you think will look/perform the best. We tend to see that letting people know what they get, rather than what they have to do, tends to work the best.
We are looking for 300x600, 300x50, 300x250, 728x90. Only one size of your choice is required but make as many as you want to showcase the different features of your design.
Animated GIFs and static images are allowed but no Flash.
Size limit is 60kbs.
Some assets are provided but you might want to refer to the web, and desktop/mobile sites for other, more current assets. The ads included are their current ads which are live right now.
Updates
Hi Everybody,
Industry/Entity Type
Law Firm

```html
<!DOCTYPE html>
<html lang="en">
<head>
<meta charset="utf-8">
<title>The Brandt Law Firm – Display Banners</title>
<link rel="stylesheet" href="https://fonts.googleapis.com/css2?family=Montserrat:wght@500&family=Open+Sans:wght@400;600;700&display=swap">
<style>
  :root {
    --board: #2a2523;
    --ink: #3a302c;
    --red: #d0392b;
    --red-dark: #b22c20;
    --white: #ffffff;
    --stone-light: #eae4dc;
    --stone-mid: #cfc6bb;
    --stone-dark: #a79c90;
    --sky: #cfe0ef;
    --photo-light: #d8d2cb;
    --photo-dark: #4a3e36;
  }
  * { box-sizing: border-box; margin: 0; padding: 0; }
  html, body { width: 1200px; height: 712px; overflow: hidden; background: var(--board); }
  .board { position: relative; width: 1131px; height: 671px; transform: scale(1.061); transform-origin: 0 0; }
  .banner { position: absolute; overflow: hidden; background: var(--white); }
  .stone { position: absolute; inset: 0; background: linear-gradient(120deg, var(--stone-light) 0%, var(--stone-mid) 45%, var(--stone-light) 70%, var(--stone-dark) 100%); }
  .services { position: absolute; list-style: none; font-family: "Montserrat", sans-serif; font-weight: 500; color: var(--ink); }
  .services li::before { content: "• "; }
  .cta { position: absolute; background: var(--red); color: var(--white); font-family: "Open Sans", sans-serif; font-weight: 600; text-align: center; display: flex; align-items: center; justify-content: center; line-height: 1.25; border: 1px solid var(--red-dark); box-shadow: 0 1px 2px rgba(0,0,0,.3); }
  .portrait { position: absolute; background: linear-gradient(180deg, var(--photo-light) 0%, #bdb3a8 45%, var(--photo-dark) 100%); }
  .phone { position: absolute; background: var(--white); display: flex; align-items: center; justify-content: center; gap: 6px; font-family: "Open Sans", sans-serif; font-weight: 600; color: var(--red); }
  .phone svg { fill: var(--ink); }
  .firm-name { position: absolute; font-family: "Open Sans", sans-serif; font-weight: 600; color: var(--red); white-space: nowrap; }
  .curve { position: absolute; left: 0; width: 100%; }

  .b-medium { left: 40px; top: 203px; width: 300px; height: 250px; }
  .b-medium .services { left: 16px; top: 11px; font-size: 17px; line-height: 23.3px; }
  .b-medium .cta { left: 11px; top: 114px; width: 116px; height: 50px; font-size: 14.5px; }
  .b-medium .phone { left: 165px; top: 50px; width: 135px; height: 27px; font-size: 14.5px; }
  .b-medium .portrait { left: 165px; top: 77px; width: 135px; height: 130px; }
  .b-medium .curve { top: 178px; height: 72px; }
  .b-medium .firm-name { left: 82px; top: 218px; font-size: 18px; }

  .b-mobile { left: 383px; top: 403px; width: 300px; height: 50px; }
  .b-mobile .curve { top: 0; height: 50px; }
  .b-mobile .firm-name { left: 97px; top: 3px; font-size: 17px; }
  .b-mobile .tagline { position: absolute; left: 127px; top: 29px; font-family: "Open Sans", sans-serif; font-weight: 600; font-size: 12.5px; color: var(--ink); }

  .b-leader { left: 40px; top: 495px; width: 728px; height: 90px; }
  .b-leader .curve { top: 0; height: 90px; }
  .b-leader .firm-name { left: 6px; top: 55px; font-size: 18px; }
  .b-leader .services { top: 20px; font-size: 15px; line-height: 23px; font-family: "Open Sans", sans-serif; font-weight: 400; }
  .b-leader .col-a { left: 226px; }
  .b-leader .col-b { left: 370px; }
  .b-leader .cta { left: 478px; top: 15px; width: 105px; height: 59px; font-size: 14.5px; }
  .b-leader .portrait { left: 590px; top: 0; width: 138px; height: 90px; }
  .b-leader .phone { left: 605px; top: 68px; width: 123px; height: 22px; font-size: 14.5px; background: rgba(255,255,255,.9); }

  .b-sky { left: 798px; top: 36px; width: 300px; height: 599px; }
  .b-sky .stone { background: linear-gradient(180deg, var(--sky) 0%, #e6e4e0 25%, var(--stone-mid) 60%, var(--stone-dark) 85%); }
  .b-sky .services { left: 20px; top: 21px; font-size: 23px; line-height: 30px; }
  .b-sky .cta { left: 22px; top: 156px; width: 256px; height: 50px; font-size: 20px; }
  .b-sky .phone { left: 30px; top: 232px; width: 243px; height: 49px; font-size: 30px; font-weight: 700; gap: 10px; }
  .b-sky .portrait { left: 30px; top: 281px; width: 243px; height: 217px; }
  .b-sky .curve { top: 462px; height: 137px; }
  .b-sky .firm-name { left: 0; width: 300px; text-align: center; top: 566px; font-size: 20px; }
</style>
</head>
<body>
<main class="board">

  <section class="banner b-medium" aria-label="300 by 250 banner">
    <div class="stone" role="img" aria-label="Marble courthouse columns background"></div>
    <ul class="services"><li>Criminal Defense</li><li>DUI Defense</li><li>White Collar</li><li>Appeals</li></ul>
    <div class="cta">Get Free<br>Legal Advise</div>
    <div class="phone"><svg width="12" height="12" viewBox="0 0 24 24"><path d="M6.6 10.8a15.1 15.1 0 0 0 6.6 6.6l2.2-2.2c.3-.3.7-.4 1-.2 1.1.4 2.3.6 3.6.6.6 0 1 .4 1 1V20c0 .6-.4 1-1 1A17 17 0 0 1 3 4c0-.6.4-1 1-1h3.5c.6 0 1 .4 1 1 0 1.3.2 2.5.6 3.6.1.3 0 .7-.2 1z"/></svg>480 555 0142</div>
    <div class="portrait" role="img" aria-label="Portrait of the two firm attorneys"></div>
    <svg class="curve" viewBox="0 0 300 72" preserveAspectRatio="none"><path d="M0 0 Q150 10 300 26 V72 H0 Z" fill="var(--red)"/><path d="M0 4 Q150 18 300 32 V72 H0 Z" fill="var(--white)"/></svg>
    <div class="firm-name">The Brandt Law Firm</div>
  </section>

  <section class="banner b-mobile" aria-label="300 by 50 banner">
    <div class="stone" role="img" aria-label="Marble courthouse columns background"></div>
    <svg class="curve" viewBox="0 0 300 50" preserveAspectRatio="none"><path d="M0 0 H86 Q74 25 82 50 H0 Z" fill="var(--red)"/><path d="M0 0 H80 Q68 25 76 50 H0 Z" fill="var(--white)"/></svg>
    <div class="firm-name">The Brandt Law Firm</div>
    <div class="tagline">Get Free Legal Advise</div>
  </section>

  <section class="banner b-leader" aria-label="728 by 90 banner">
    <div class="stone" role="img" aria-label="Marble courthouse columns background"></div>
    <svg class="curve" viewBox="0 0 728 90" preserveAspectRatio="none"><path d="M0 0 H220 Q206 45 212 90 H0 Z" fill="var(--red)"/><path d="M0 0 H212 Q198 45 204 90 H0 Z" fill="var(--white)"/></svg>
    <div class="firm-name">The Brandt Law Firm</div>
    <ul class="services col-a"><li>Criminal Defense</li><li>DUI Defense</li></ul>
    <ul class="services col-b"><li>White Collar</li><li>Appeals</li></ul>
    <div class="cta">Get Free<br>Legal Advise</div>
    <div class="portrait" role="img" aria-label="Portrait of the two firm attorneys"></div>
    <div class="phone"><svg width="11" height="11" viewBox="0 0 24 24"><path d="M6.6 10.8a15.1 15.1 0 0 0 6.6 6.6l2.2-2.2c.3-.3.7-.4 1-.2 1.1.4 2.3.6 3.6.6.6 0 1 .4 1 1V20c0 .6-.4 1-1 1A17 17 0 0 1 3 4c0-.6.4-1 1-1h3.5c.6 0 1 .4 1 1 0 1.3.2 2.5.6 3.6.1.3 0 .7-.2 1z"/></svg>480 555 0142</div>
  </section>

  <section class="banner b-sky" aria-label="300 by 600 banner">
    <div class="stone" role="img" aria-label="Courthouse columns against a pale sky"></div>
    <ul class="services"><li>Criminal Defense</li><li>DUI Defense</li><li>White Collar</li><li>Appeals</li></ul>
    <div class="cta">Get Free Legal Advise</div>
    <div class="phone"><svg width="26" height="26" viewBox="0 0 24 24"><path d="M6.6 10.8a15.1 15.1 0 0 0 6.6 6.6l2.2-2.2c.3-.3.7-.4 1-.2 1.1.4 2.3.6 3.6.6.6 0 1 .4 1 1V20c0 .6-.4 1-1 1A17 17 0 0 1 3 4c0-.6.4-1 1-1h3.5c.6 0 1 .4 1 1 0 1.3.2 2.5.6 3.6.1.3 0 .7-.2 1z"/></svg>480 555 0142</div>
    <div class="portrait" role="img" aria-label="Portrait of the two firm attorneys"></div>
    <svg class="curve" viewBox="0 0 300 137" preserveAspectRatio="none"><path d="M0 0 Q150 20 300 34 V137 H0 Z" fill="var(--red)"/><path d="M0 6 Q150 30 300 42 V137 H0 Z" fill="var(--white)"/></svg>
    <div class="firm-name">The Brandt Law Firm</div>
  </section>

</main>
</body>
</html>
```